Flyer Design for a Boston Therapeutic Clinic

I am a body therapist who needs a couple of flyers designed:
1. To fit half a page.
2. To fit a 5 inch by 3.5 inch flyer.
My practice is based in Boston, MA and my web site is:
www.LarchTessvik.Com
For the First half page:
A. Have my company's name and color shown as it appears on my web site (Larch Tessvik)
B. Have the following text: "Control your weight (This part should be emphasized) by balancing your nervous and digestive system through the Tessvik Method. The Tessvik Method, a technique developed by Dr. Mara. Tessvik, uses physical pressure to manipulate visceral tissue to bring back resiliency and proper functioning of the whole body."
Also helps with
-Constipation
-Bloating
-IBS
-eating disorders and overeating
Our practitioner is highly experienced. Please visit our web sites for reviews.
C. I would like to have a nice earthy feeling, something that feels "freeing" like open flowers, or an open land scape such as mountains or fields.
D. I also like the color blue, white, orange; perhaps if these colors can be integrated into the flyer, that would be great.
E. "Visit our web site LarchTessvik.com or call 786-555-0148"
The Smaller Flyer :
A.The smaller Flyer should also have my Company's name as shown on my web site (Larch Tessvik)
B.The following text: " Restore your body's natural resiliency and greatly reduce your physical pain through the Dr. Mara Tessvik Method of Structural Integration."
C. "Our practitioner is highly experienced and has a great reputation; visit our web site for reviews."
"Benefits:
"reduce aches and pains
reduce joint pain
reduce chronic muscular tension"
D, "feel better after the first session!"
E. if you could use a picture of me working on someone from my web site, that would be great.
F. I also like the colors white, orange and silver, for this one.
G. "Visit our web site LarchTessvik.com or call 786-555 0148"
I am very open minded,
I would like the flyer to evoke a sense of tranquility, professionalism, and simplicity. So if you have another angle you think would look good, then go for it! As long as it looks clean, professional and helpful.
Thanks a lot!
If you need any pictures from my web site, I have the original high resolution files that i can send.
Professionals and working men and women from ages 20-70
Clinic

```html
<!DOCTYPE html>
<html lang="en">
<head>
<meta charset="utf-8">
<title>Larch Tessvik Therapy – Flyers</title>
<link rel="stylesheet" href="https://fonts.googleapis.com/css2?family=Passion+One:wght@400;700&family=Questrial&family=Roboto+Slab:wght@400;700&family=Zilla+Slab:wght@300;400&family=Titan+One&family=Open+Sans:wght@600;700&display=swap">
<style>
  :root {
    --bg: #3a3a3a;
    --paper: #f4f2f0;
    --paper-shade: #dcdad8;
    --blue: #1a5fb4;
    --blue-bright: #1e88e5;
    --orange: #f0561c;
    --orange-deep: #d9400f;
    --orange-warm: #f7941d;
    --ink: #1c1c1c;
    --grey: #4a4a4a;
    --grey-mid: #6f6f6f;
    --silver: #bdbdbd;
    --black: #111;
    --white: #fff;
  }
  * { margin: 0; padding: 0; box-sizing: border-box; }
  html, body { width: 1200px; height: 842px; overflow: hidden; }
  body { background: var(--bg); position: relative; font-family: "Questrial", sans-serif; }

  .flyer { position: absolute; overflow: hidden; box-shadow: 0 6px 18px rgba(0,0,0,.45); }

  /* ---------- Half-page flyer ---------- */
  .flyer--half {
    left: 47px; top: 95px; width: 496px; height: 678px;
    background: linear-gradient(180deg, var(--paper) 0%, var(--paper) 60%, var(--paper-shade) 100%);
  }
  .flyer--half .hero { position: absolute; left: 0; top: 0; width: 496px; height: 320px; }
  .flyer--half .detail-photo {
    position: absolute; left: 260px; top: 330px; width: 236px; height: 300px;
    background: radial-gradient(ellipse at 60% 40%, rgba(150,150,150,.45), rgba(244,242,240,0) 70%);
  }
  .headline { position: absolute; right: 32px; top: 222px; text-align: right; font-family: "Passion One", sans-serif; line-height: .9; }
  .headline__main { display: block; font-size: 66px; font-weight: 700; color: var(--blue); letter-spacing: 1px; -webkit-text-stroke: 1.5px #fff; }
  .headline__sub { display: block; font-size: 40px; font-weight: 700; color: var(--orange); letter-spacing: 1px; -webkit-text-stroke: 1px #fff; }
  .intro { position: absolute; left: 16px; top: 333px; width: 470px; font-size: 11.6px; line-height: 15.4px; color: var(--ink); }
  .helps-title { position: absolute; left: 16px; top: 405px; font-family: "Roboto Slab", serif; font-weight: 700; font-size: 18px; color: var(--blue); letter-spacing: .5px; }
  .helps-list { position: absolute; left: 10px; top: 434px; list-style: none; }
  .helps-list li, .benefits-list li { position: relative; padding-left: 16px; font-size: 13.5px; line-height: 19px; color: var(--ink); }
  .helps-list li::before, .benefits-list li::before { content: ""; position: absolute; left: 0; top: 5px; width: 9px; height: 9px; border-radius: 50%; background: var(--orange); }
  .reviews-note { position: absolute; left: 16px; top: 520px; font-size: 11.2px; line-height: 16px; color: var(--orange-deep); letter-spacing: .3px; }
  .divider { position: absolute; left: 16px; top: 568px; width: 460px; height: 1px; background: #9a9a9a; }
  .brand { position: absolute; left: 0; width: 496px; top: 580px; text-align: center; font-family: "Roboto Slab", serif; font-weight: 700; font-size: 21px; letter-spacing: 1px; }
  .brand__first { color: var(--blue); }
  .brand__rest { color: var(--grey); }
  .phone { position: absolute; display: flex; align-items: center; gap: 8px; font-family: "Questrial", sans-serif; }
  .flyer--half .phone { left: 74px; top: 618px; font-size: 43px; color: var(--orange); }
  .flyer--half .phone svg { width: 32px; height: 32px; fill: var(--grey); }
  .flyer--half .base-line { position: absolute; left: 0; bottom: 0; width: 496px; height: 5px; background: var(--blue); }

  /* ---------- Small flyer ---------- */
  .flyer--small { left: 715px; top: 180px; width: 428px; height: 615px; background: var(--white); }
  .flyer--small .hero { position: absolute; left: 0; top: 0; width: 428px; height: 185px; }
  .title { position: absolute; right: 16px; top: 0; text-align: right; font-family: "Zilla Slab", serif; font-weight: 300; color: var(--white); }
  .title__name { display: block; font-size: 55px; line-height: 60px; letter-spacing: 2px; }
  .title__rest { display: block; font-size: 31px; line-height: 30px; letter-spacing: 1px; }
  .lead { position: absolute; left: 11px; top: 192px; width: 270px; font-family: "Open Sans", sans-serif; font-weight: 600; font-size: 12.3px; line-height: 16px; color: var(--black); }
  .reputation { position: absolute; left: 11px; top: 274px; width: 340px; font-family: "Zilla Slab", serif; font-size: 14.6px; line-height: 18.5px; letter-spacing: 1px; color: var(--grey-mid); }
  .practitioner-photo { position: absolute; left: 190px; top: 325px; width: 238px; height: 185px; }
  .benefits-banner { position: absolute; left: 0; top: 365px; width: 200px; height: 24px; }
  .benefits-banner span { position: absolute; left: 10px; top: 1px; font-family: "Roboto Slab", serif; font-weight: 700; font-size: 17px; color: var(--white); letter-spacing: 1px; }
  .benefits-list { position: absolute; left: 10px; top: 400px; list-style: none; width: 250px; }
  .benefits-list li { font-family: "Zilla Slab", serif; font-size: 15px; line-height: 12px; margin-bottom: 12px; color: var(--grey); letter-spacing: .5px; }
  .benefits-list li::before { top: 2px; }
  .session-strip { position: absolute; left: 0; top: 505px; width: 428px; height: 38px; }
  .session-strip span { position: absolute; left: 0; width: 420px; top: 7px; text-align: center; font-family: "Titan One", sans-serif; font-size: 15px; color: var(--white); font-style: italic; letter-spacing: .5px; }
  .phone-band { position: absolute; left: 0; top: 543px; width: 428px; height: 50px; background: linear-gradient(180deg, #fff, #e6e6e6); }
  .flyer--small .phone { left: 74px; top: 545px; font-size: 38px; color: var(--ink); }
  .flyer--small .phone svg { width: 28px; height: 28px; fill: var(--ink); }
  .web-bar { position: absolute; left: 0; bottom: 0; width: 428px; height: 22px; background: var(--black); text-align: center; font-family: "Zilla Slab", serif; font-size: 12.5px; line-height: 22px; color: var(--white); letter-spacing: 3px; }
</style>
</head>
<body>

<!-- Half-page flyer -->
<section class="flyer flyer--half" aria-label="Half-page flyer">
  <svg class="hero" viewBox="0 0 496 320" aria-hidden="false">
    <defs>
      <linearGradient id="portraitTone" x1="0" y1="0" x2="1" y2="0">
        <stop offset="0" stop-color="#3c3c3c"/><stop offset=".6" stop-color="#8a8a8a"/><stop offset="1" stop-color="#c4c4c4"/>
      </linearGradient>
      <radialGradient id="anatomyTone" cx=".55" cy=".45" r=".55">
        <stop offset="0" stop-color="#e8501c"/><stop offset=".6" stop-color="#9c2410"/><stop offset="1" stop-color="#1a0a06"/>
      </radialGradient>
    </defs>
    <rect width="496" height="320" fill="#f4f2f0"/>
    <rect width="496" height="280" fill="url(#portraitTone)" role="img" aria-label="Black and white photo of a thoughtful man with a faint skeleton overlay"/>
    <path d="M160 290 C260 200 330 80 496 40 L496 300 L160 300 Z" fill="#0d0d0d"/>
    <path d="M250 290 C320 200 360 110 496 70 L496 240 C430 270 330 290 250 290 Z" fill="url(#anatomyTone)" role="img" aria-label="Illustration of a glowing red human ribcage and torso"/>
    <path d="M330 30 C400 0 450 5 496 0 L496 40 C420 40 360 60 300 100 C300 70 310 45 330 30 Z" fill="var(--orange)"/>
    <path d="M0 300 C60 280 130 245 200 210 C150 260 90 300 20 320 L0 320 Z" fill="var(--blue-bright)"/>
    <path d="M0 320 C120 300 200 260 260 230 C220 280 160 310 80 320 Z" fill="#f4f2f0"/>
  </svg>
  <div class="detail-photo" role="img" aria-label="Faded grey photo of hands giving a therapy treatment"></div>

  <h1 class="headline"><span class="headline__main">CONTROL</span><span class="headline__sub">YOUR WEIGHT</span></h1>

  <p class="intro">by balancing your nervous and digestive system through the Tessvik Method. The Tessvik Method, a technique developed by Dr. Mara. Tessvik, uses physical pressure to manipulate visceral tissue to bring back resiliency and proper functioning of the whole body.</p>

  <h2 class="helps-title">ALSO HELPS WITH</h2>
  <ul class="helps-list">
    <li>Constipation</li>
    <li>Bloating</li>
    <li>IBS</li>
    <li>Psychological eating disorders</li>
  </ul>

  <p class="reviews-note">OUR PRACTITIONER IS HIGHLY EXPERIENCED.<br>PLEASE VISIT OUR WEB SITES FOR REVIEWS</p>
  <div class="divider"></div>
  <p class="brand"><span class="brand__first">Larch</span> <span class="brand__rest">Tessvik Therapy</span></p>
  <p class="phone">
    <svg viewBox="0 0 24 24" aria-hidden="true"><path d="M6.6 10.8a15.1 15.1 0 0 0 6.6 6.6l2.2-2.2a1 1 0 0 1 1-.25 11.4 11.4 0 0 0 3.6.57 1 1 0 0 1 1 1V20a1 1 0 0 1-1 1A17 17 0 0 1 3 4a1 1 0 0 1 1-1h3.5a1 1 0 0 1 1 1c0 1.25.2 2.45.57 3.57a1 1 0 0 1-.25 1z"/></svg>
    <span>786-555-0148</span>
  </p>
  <div class="base-line"></div>
</section>

<!-- Small flyer -->
<section class="flyer flyer--small" aria-label="Small flyer">
  <svg class="hero" viewBox="0 0 428 185">
    <defs>
      <linearGradient id="massageTone" x1="0" y1="0" x2="1" y2="1">
        <stop offset="0" stop-color="#f7a21b"/><stop offset=".5" stop-color="#e8661a"/><stop offset="1" stop-color="#c23a12"/>
      </linearGradient>
    </defs>
    <rect width="428" height="185" fill="url(#massageTone)" role="img" aria-label="Warm orange-toned photo of a woman relaxing during a back massage"/>
    <path d="M0 150 C150 135 300 140 428 170 L428 185 L0 185 Z" fill="#8f8f8f"/>
    <path d="M0 158 C150 145 300 150 428 178 L428 185 L0 185 Z" fill="#fff"/>
  </svg>
  <h1 class="title"><span class="title__name">Larch</span><span class="title__rest">Tessvik Therapy</span></h1>

  <p class="lead">Restore your body's natural resiliency and greatly reduce your physical pain through the Dr. Mara Tessvik Method of Structural Integration.</p>
  <p class="reputation">OUR PRACTITIONER IS HIGHLY EXPERIENCED AND HAS A GREAT REPUTATION; VISIT OUR WEB SITE FOR REVIEWS</p>

  <svg class="practitioner-photo" viewBox="0 0 238 185" role="img" aria-label="Photo of the therapist working on a client's shoulder">
    <defs>
      <radialGradient id="practTone" cx=".55" cy=".5" r=".6">
        <stop offset="0" stop-color="#8a6a58"/><stop offset=".55" stop-color="#c9a08a"/><stop offset="1" stop-color="#fff" stop-opacity="0"/>
      </radialGradient>
    </defs>
    <rect width="238" height="185" fill="url(#practTone)"/>
  </svg>

  <svg class="benefits-banner" viewBox="0 0 200 24" aria-hidden="true">
    <path d="M0 0 H178 L200 24 H0 Z" fill="var(--orange)"/>
    <path d="M178 0 L200 24 H190 L170 2 Z" fill="var(--black)"/>
  </svg>
  <div class="benefits-banner"><span>BENEFITS:</span></div>

  <ul class="benefits-list">
    <li>reduce aches and pain</li>
    <li>reduce joint pain</li>
    <li>reduce chronic muscular tension</li>
  </ul>

  <svg class="session-strip" viewBox="0 0 428 38" aria-hidden="true">
    <defs>
      <linearGradient id="stripTone" x1="0" y1="0" x2="1" y2="0">
        <stop offset="0" stop-color="#f7941d"/><stop offset="1" stop-color="#e8401a"/>
      </linearGradient>
    </defs>
    <rect width="428" height="38" fill="#e8661a"/>
    <path d="M0 5 H428 L420 33 H0 Z" fill="url(#stripTone)"/>
    <path d="M410 5 H428 L420 33 H402 Z" fill="#6a6a6a"/>
  </svg>
  <div class="session-strip"><span>FEEL BETTER AFTER THE FIRST SESSION!</span></div>

  <div class="phone-band"></div>
  <p class="phone">
    <svg viewBox="0 0 24 24" aria-hidden="true"><path d="M6.6 10.8a15.1 15.1 0 0 0 6.6 6.6l2.2-2.2a1 1 0 0 1 1-.25 11.4 11.4 0 0 0 3.6.57 1 1 0 0 1 1 1V20a1 1 0 0 1-1 1A17 17 0 0 1 3 4a1 1 0 0 1 1-1h3.5a1 1 0 0 1 1 1c0 1.25.2 2.45.57 3.57a1 1 0 0 1-.25 1z"/></svg>
    <span>786-555-0148</span>
  </p>
  <p class="web-bar">www.LarchTessvik.com</p>
</section>

</body>
</html>
```